"MEET THE TEAM" page web design

We need a "meet the team" page for our website!
Please look at our website to see the style we need

We are looking for something unique, fun, cool, technology-style and yet professional. We plan on taking a picture of each employee (not sure if this will be a real photo/caricature/ black and white/goofy picture--> but we are open to any ideas you have that will work with the design) and putting it there, along with a little bio about each person.

Thanks! looking forward to working together:)
Updates

Project Deadline Extended
Reason: I am excited to see more designs and find the perfect fit. Thanks designers :)

Target Market(s)

People looking to purchase servers, workstations, components

Industry/Entity Type

Information Technology

Number of Pages Required

1 page

Font styles to use
Sans Serif
Other font styles liked:
• The font we use on our site so it matches

Requirements
Must have
• please look at our website qondimex.com and see the theme and colors we want.
• We have 13 employees but would like to have a design where we can add/remove people if we hire/terminate them without messing up the design.
• We are looking for something unique, fun, cool, technology-style and yet professional. We plan on taking a picture of each employee (not sure if this will be a real photo/caricature/ black and white/goofy picture--> but we are open to any ideas you have that will work with the design) and putting it there, along with a little bio about each person.
• We can upload anything you need
Nice to have
• We are also interested in having a design where when the cursor moves over a person then the bio comes out or moves around, or something. (This is not required, but we would love some cool ideas) And if you can come up with some design, we would have our programmers create it for us.
Should not have
• we are open to anything

```html
<!DOCTYPE html>
<html lang="en">
<head>
<meta charset="utf-8">
<title>Meet Our Team – Qondimex</title>
<link href="https://fonts.googleapis.com/css2?family=Montserrat:wght@300;400;500;600&family=Open+Sans:wght@400;600&display=swap" rel="stylesheet">
<style>
:root{
  --teal:#1aa89c;
  --teal-light:#4fc2b8;
  --ink:#4a4a4a;
  --muted:#8a8a8a;
  --rule:#e4e4e4;
  --intro-bg:#f5f5f5;
  --footer:#a3a3a3;
  --footer-dark:#8e8e8e;
  --white:#fff;
}
*{box-sizing:border-box;margin:0;padding:0}
html,body{width:1200px;height:2267px;overflow:hidden;background:var(--white)}
body{font-family:"Open Sans",Arial,sans-serif;color:var(--ink)}
.wrap{width:1034px;margin-left:84px;position:relative}

/* header */
.top{height:100px;position:relative;border-bottom:1px solid var(--rule)}
.brand{position:absolute;left:84px;top:30px;display:flex;align-items:center;gap:14px}
.brand-dot{width:40px;height:40px;border-radius:50%;background:var(--teal)}
.brand-name{font-family:"Montserrat",sans-serif;font-weight:500;font-size:32px;letter-spacing:3px;color:var(--teal)}
.account{position:absolute;right:82px;top:0;display:flex;height:28px;border-radius:0 0 16px 16px;overflow:hidden;font-family:"Montserrat",sans-serif;font-size:9px;letter-spacing:.5px}
.account a{display:flex;align-items:center;justify-content:center;width:87px;color:#444;text-decoration:none;background:#cfcfcf}
.account a+a{background:#b0b0b0}
.contact-top{position:absolute;right:82px;top:56px;display:flex;align-items:center;gap:28px;font-family:"Montserrat",sans-serif}
.contact-top span{display:flex;align-items:center;gap:12px}
.ring{width:32px;height:32px;border-radius:50%;border:1px solid #cfe9e6;display:flex;align-items:center;justify-content:center}
.chat{color:var(--teal);font-size:15px;letter-spacing:1px}
.phone-top{color:#555;font-size:16px;letter-spacing:1px}

.nav{height:52px;position:relative;border-bottom:1px solid var(--rule)}
.nav ul{list-style:none;position:absolute;left:84px;top:0;height:50px;display:flex;align-items:center;gap:32px;font-family:"Montserrat",sans-serif;font-size:10px;color:#777;letter-spacing:.4px}
.search{position:absolute;left:917px;top:8px;width:151px;height:38px;border:1px solid #bbb;border-radius:19px;font-size:10px;color:#777;padding:12px 18px}
.search svg{position:absolute;right:14px;top:10px}
.cart{position:absolute;left:1080px;top:8px;width:38px;height:38px;border:1px solid #bbb;border-radius:50%;display:flex;align-items:center;justify-content:center}

.crumbs{height:38px;background:var(--teal);font-family:"Montserrat",sans-serif;font-size:10px;font-weight:600;color:var(--white);letter-spacing:.5px;display:flex;align-items:center;padding-left:84px;gap:10px}
.crumbs .here{color:#2b6f69}

/* intro */
.intro{height:302px;background:var(--intro-bg);padding-top:50px}
.intro h1{font-family:"Montserrat",sans-serif;font-weight:400;font-size:25px;letter-spacing:2.5px;color:#444}
.accent{width:30px;height:2px;background:var(--teal);margin:22px 0 20px}
.lead{font-weight:600;font-size:14px;line-height:22px;color:#555;width:830px}
.intro p.body{margin-top:20px;font-size:11px;line-height:20px;color:var(--muted);width:1034px}

/* team members */
.member{display:grid;align-items:start;border-bottom:1px solid var(--rule)}
.member.portrait-right{grid-template-columns:265px 184px 536px;column-gap:49px}
.member.portrait-left{grid-template-columns:184px 238px 536px;column-gap:76px 0}
.member.portrait-left .info{margin-left:76px}
.member.portrait-left{column-gap:0}
.member.portrait-left .bio{margin-left:0}
.member.last{border-bottom:none}
.role{font-family:"Montserrat",sans-serif;font-size:14px;color:var(--teal);letter-spacing:.5px}
.name{font-family:"Montserrat",sans-serif;font-weight:300;font-size:25px;color:#555;margin-top:6px;letter-spacing:.3px}
.info .accent{background:#ccc;width:30px;height:1px;margin:18px 0 16px}
.details{list-style:none;font-size:11px;line-height:24px;color:var(--muted)}
.details li{display:flex;align-items:center;gap:10px}
.details .mail{color:var(--teal)}
.social-sm{display:flex;gap:8px;margin-top:10px}
.social-sm span{width:24px;height:24px;border:1px solid #ccc;border-radius:50%}
.portrait{width:184px;height:184px;border-radius:50%;border:2px solid var(--teal);background:radial-gradient(circle at 50% 40%,#e9d5c3 0,#c9a27c 45%,#3a3230 100%)}
.bio{font-size:11px;line-height:19.5px;color:var(--muted)}
.bio p+p{margin-top:18px}

/* footer */
.footer{height:416px;background:var(--footer);color:var(--white);text-align:center;padding-top:48px}
.footer .about{font-size:14px;line-height:24px;width:760px;margin:0 auto}
.footer .divider{width:350px;height:1px;background:#bdbdbd;margin:44px auto 32px}
.f-contacts{display:flex;justify-content:center;gap:80px;font-size:12px;text-align:left}
.f-contacts div{display:flex;gap:12px;align-items:flex-start;line-height:20px}
.f-links{display:flex;justify-content:center;gap:62px;margin-top:52px;font-size:14px}
.f-links ul{list-style:none;font-size:10px;line-height:14px;margin-top:12px;text-align:center}
.bottom{height:209px;background:var(--footer-dark);text-align:center;padding-top:24px;color:var(--white)}
.social{display:flex;justify-content:center;gap:12px}
.social span{width:33px;height:33px;border:1px solid #c7c7c7;border-radius:50%}
.bottom .line{width:900px;height:1px;background:#a3a3a3;margin:24px auto 28px}
.mark{width:28px;height:28px;border-radius:50%;background:#c4c4c4;margin:0 auto}
.copy{font-size:10.5px;margin-top:18px}
</style>
</head>
<body>
<header>
  <div class="top">
    <div class="brand"><span class="brand-dot"></span><span class="brand-name">QONDIMEX</span></div>
    <div class="account"><a href="#">SIGN UP</a><a href="#">LOGIN</a></div>
    <div class="contact-top">
      <span class="chat"><span class="ring"><svg width="14" height="12" viewBox="0 0 14 12"><path d="M2 1h10a1 1 0 0 1 1 1v6a1 1 0 0 1-1 1H6l-3 2V9H2a1 1 0 0 1-1-1V2a1 1 0 0 1 1-1z" fill="#1aa89c"/></svg></span>LIVE CHAT</span>
      <span class="phone-top"><span class="ring"><svg width="14" height="14" viewBox="0 0 14 14"><path d="M3 1l2 3-1.5 1.5a8 8 0 0 0 5 5L10 9l3 2-1.5 2C6 13 1 8 1 2.5z" fill="#1aa89c"/></svg></span>415-555-0172</span>
    </div>
  </div>
  <nav class="nav">
    <ul><li>SERVER</li><li>WORKSTATION</li><li>COMPONENTS</li><li>VIRTUAL REALITY</li><li>DRONES</li><li>ABOUT US</li><li>BLOG</li><li>RESOURCES</li><li>CONTACT US</li></ul>
    <div class="search">Search<svg width="16" height="16" viewBox="0 0 16 16"><circle cx="7" cy="7" r="5.5" fill="none" stroke="#1aa89c" stroke-width="1.5"/><path d="M11 11l4 4" stroke="#1aa89c" stroke-width="1.5"/></svg></div>
    <div class="cart"><svg width="18" height="16" viewBox="0 0 18 16"><path d="M1 1h3l2 9h9l2-6H5" fill="none" stroke="#1aa89c" stroke-width="1.6"/><circle cx="7" cy="13.5" r="1.5" fill="#1aa89c"/><circle cx="14" cy="13.5" r="1.5" fill="#1aa89c"/></svg></div>
  </nav>
  <div class="crumbs"><span>HOME</span><span>/</span><span>ABOUT US</span><span>/</span><span class="here">TEAM</span></div>
</header>

<main>
  <section class="intro">
    <div class="wrap">
      <h1>MEET OUR TEAM</h1>
      <div class="accent"></div>
      <p class="lead">Qondimex, LLC provides Enterprise IT Hardware in the same quality of service and equipment that major brands provide without the major brand pricing.</p>
      <p class="body">Lorem ipsum dolor sit amet, consectetur adipiscing elit, sed do eiusmod tempor incididunt ut labore et dolore magna aliqua. Ut enim ad minim veniam, quis nostrud exercitation ullamco laboris nisi ut aliquip ex ea commodo consequat. Duis aute irure dolor in reprehenderit in voluptate velit esse cillum dolore eu fugiat nulla pariatur. Excepteur sint occaecat cupidatat non proident, sunt in culpa qui officia deserunt mollit anim id est laborum.</p>
    </div>
  </section>

  <article class="wrap member portrait-right" style="height:283px;padding-top:50px">
    <div class="info">
      <div class="role">CO FOUNDER</div>
      <div class="name">Corin D. Maswell</div>
      <div class="accent"></div>
      <ul class="details">
        <li><svg width="10" height="12" viewBox="0 0 10 12"><circle cx="6" cy="2" r="1.6" fill="#999"/><path d="M5 4L3 8l-2 3M5 4l1 4 2 3M4 5l3 1" stroke="#999" stroke-width="1.2" fill="none"/></svg>corindmaswell</li>
        <li class="mail"><svg width="11" height="8" viewBox="0 0 11 8"><rect width="11" height="8" rx="1" fill="#1aa89c"/><path d="M0 0l5.5 4.5L11 0" stroke="#fff" fill="none"/></svg>corind@qondimex.com</li>
        <li><svg width="10" height="10" viewBox="0 0 14 14"><path d="M3 1l2 3-1.5 1.5a8 8 0 0 0 5 5L10 9l3 2-1.5 2C6 13 1 8 1 2.5z" fill="#999"/></svg>(+91) 5550 1234</li>
      </ul>
      <div class="social-sm"><span></span><span></span></div>
    </div>
    <div class="portrait" role="img" aria-label="Portrait illustration of the co founder"></div>
    <div class="bio">
      <p>Lorem ipsum dolor sit amet, consectetur adipiscing elit, sed do eiusmod tempor incididunt ut labore et dolore magna aliqua. Ut enim ad minim veniam, quis nostrud exercitation ullamco laboris nisi ut aliquip ex ea commodo consequat. Duis aute irure dolor in reprehenderit in voluptate velit esse cillum dolore eu fugiat nulla pariatur. Excepteur sint occaecat cupidatat non proident, sunt in culpa qui officia deserunt mollit anim id est laborum.</p>
      <p>Ut enim ad minim veniam, quis nostrud exercitation ullamco laboris nisi ut aliquip ex ea commodo consequat.</p>
    </div>
  </article>

  <article class="wrap member portrait-left" style="height:280px;padding-top:50px">
    <div class="portrait" role="img" aria-label="Portrait illustration of the director"></div>
    <div class="info">
      <div class="role">DIRECTOR</div>
      <div class="name">Elias Brandt</div>
      <div class="accent"></div>
      <ul class="details">
        <li><svg width="10" height="12" viewBox="0 0 10 12"><circle cx="6" cy="2" r="1.6" fill="#999"/><path d="M5 4L3 8l-2 3M5 4l1 4 2 3M4 5l3 1" stroke="#999" stroke-width="1.2" fill="none"/></svg>eliasbrandt</li>
        <li class="mail"><svg width="11" height="8" viewBox="0 0 11 8"><rect width="11" height="8" rx="1" fill="#1aa89c"/><path d="M0 0l5.5 4.5L11 0" stroke="#fff" fill="none"/></svg>corind@qondimex.com</li>
        <li><svg width="10" height="10" viewBox="0 0 14 14"><path d="M3 1l2 3-1.5 1.5a8 8 0 0 0 5 5L10 9l3 2-1.5 2C6 13 1 8 1 2.5z" fill="#999"/></svg>(+91) 5550 1234</li>
      </ul>
      <div class="social-sm"><span></span><span></span></div>
    </div>
    <div class="bio">
      <p>Lorem ipsum dolor sit amet, consectetur adipiscing elit, sed do eiusmod tempor incididunt ut labore et dolore magna aliqua. Ut enim ad minim veniam, quis nostrud exercitation ullamco laboris nisi ut aliquip ex ea commodo consequat. Duis aute irure dolor in reprehenderit in voluptate velit esse cillum dolore eu fugiat nulla pariatur. Excepteur sint occaecat cupidatat non proident, sunt in culpa qui officia deserunt mollit anim id est laborum.</p>
      <p>Ut enim ad minim veniam, quis nostrud exercitation ullamco laboris nisi ut aliquip ex ea commodo consequat.</p>
    </div>
  </article>

  <article class="wrap member portrait-right" style="height:275px;padding-top:45px">
    <div class="info">
      <div class="role">CO FOUNDER</div>
      <div class="name">Corin D. Maswell</div>
      <div class="accent"></div>
      <ul class="details">
        <li><svg width="10" height="12" viewBox="0 0 10 12"><circle cx="6" cy="2" r="1.6" fill="#999"/><path d="M5 4L3 8l-2 3M5 4l1 4 2 3M4 5l3 1" stroke="#999" stroke-width="1.2" fill="none"/></svg>corindmaswell</li>
        <li class="mail"><svg width="11" height="8" viewBox="0 0 11 8"><rect width="11" height="8" rx="1" fill="#1aa89c"/><path d="M0 0l5.5 4.5L11 0" stroke="#fff" fill="none"/></svg>corind@qondimex.com</li>
        <li><svg width="10" height="10" viewBox="0 0 14 14"><path d="M3 1l2 3-1.5 1.5a8 8 0 0 0 5 5L10 9l3 2-1.5 2C6 13 1 8 1 2.5z" fill="#999"/></svg>(+91) 5550 1234</li>
      </ul>
      <div class="social-sm"><span></span><span></span></div>
    </div>
    <div class="portrait" role="img" aria-label="Portrait illustration of a team member with blonde hair" style="background:radial-gradient(circle at 50% 40%,#f0dcc6 0,#d9d27a 50%,#3a3230 100%)"></div>
    <div class="bio">
      <p>Lorem ipsum dolor sit amet, consectetur adipiscing elit, sed do eiusmod tempor incididunt ut labore et dolore magna aliqua. Ut enim ad minim veniam, quis nostrud exercitation ullamco laboris nisi ut aliquip ex ea commodo consequat. Duis aute irure dolor in reprehenderit in voluptate velit esse cillum dolore eu fugiat nulla pariatur. Excepteur sint occaecat cupidatat non proident, sunt in culpa qui officia deserunt mollit anim id est laborum.</p>
      <p>Ut enim ad minim veniam, quis nostrud exercitation ullamco laboris nisi ut aliquip ex ea commodo consequat.</p>
    </div>
  </article>

  <article class="wrap member portrait-left last" style="height:312px;padding-top:50px">
    <div class="portrait" role="img" aria-label="Portrait illustration of the director"></div>
    <div class="info">
      <div class="role">DIRECTOR</div>
      <div class="name">Elias Brandt</div>
      <div class="accent"></div>
      <ul class="details">
        <li><svg width="10" height="12" viewBox="0 0 10 12"><circle cx="6" cy="2" r="1.6" fill="#999"/><path d="M5 4L3 8l-2 3M5 4l1 4 2 3M4 5l3 1" stroke="#999" stroke-width="1.2" fill="none"/></svg>eliasbrandt</li>
        <li class="mail"><svg width="11" height="8" viewBox="0 0 11 8"><rect width="11" height="8" rx="1" fill="#1aa89c"/><path d="M0 0l5.5 4.5L11 0" stroke="#fff" fill="none"/></svg>corind@qondimex.com</li>
        <li><svg width="10" height="10" viewBox="0 0 14 14"><path d="M3 1l2 3-1.5 1.5a8 8 0 0 0 5 5L10 9l3 2-1.5 2C6 13 1 8 1 2.5z" fill="#999"/></svg>(+91) 5550 1234</li>
      </ul>
      <div class="social-sm"><span></span><span></span></div>
    </div>
    <div class="bio">
      <p>Lorem ipsum dolor sit amet, consectetur adipiscing elit, sed do eiusmod tempor incididunt ut labore et dolore magna aliqua. Ut enim ad minim veniam, quis nostrud exercitation ullamco laboris nisi ut aliquip ex ea commodo consequat. Duis aute irure dolor in reprehenderit in voluptate velit esse cillum dolore eu fugiat nulla pariatur. Excepteur sint occaecat cupidatat non proident, sunt in culpa qui officia deserunt mollit anim id est laborum.</p>
      <p>Ut enim ad minim veniam, quis nostrud exercitation ullamco laboris nisi ut aliquip ex ea commodo consequat.</p>
    </div>
  </article>
</main>

<footer>
  <div class="footer">
    <p class="about">Based in Halden Park California, Qondimex offers custom servers, storage, and workstations for local businesses in Los Angeles, Beverly Hills, Thousand Oaks, Ventura, Orange County, Santa Barbara, Oxnard, Irvine, Anaheim, and San Diego. Qondimex also offers such products to clients throughout the United States and Worldwide.</p>
    <div class="divider"></div>
    <div class="f-contacts">
      <div><svg width="12" height="16" viewBox="0 0 12 16"><path d="M6 15S1 9 1 6a5 5 0 0 1 10 0c0 3-5 9-5 9z" fill="none" stroke="#fff"/><circle cx="6" cy="6" r="2" fill="none" stroke="#fff"/></svg><span>2280 Larkfield Ave.<br>Halden Park, CA 91390</span></div>
      <div><svg width="14" height="14" viewBox="0 0 14 14"><path d="M3 1l2 3-1.5 1.5a8 8 0 0 0 5 5L10 9l3 2-1.5 2C6 13 1 8 1 2.5z" fill="none" stroke="#fff"/></svg><span>415-555-0173</span></div>
      <div><svg width="15" height="11" viewBox="0 0 15 11"><rect x=".5" y=".5" width="14" height="10" fill="none" stroke="#fff"/><path d="M.5.5l7 5 7-5" fill="none" stroke="#fff"/></svg><span>sales@qondimex.com</span></div>
    </div>
    <div class="f-links">
      <div>Computer Hardware</div>
      <div>Drones</div>
      <div>Virtual Reality</div>
      <div>About Us</div>
      <div>Customer Support
        <ul><li>Terms and Conditions</li><li>Warranty Information</li><li>Contact Us</li><li>Return Policy</li></ul>
      </div>
    </div>
  </div>
  <div class="bottom">
    <div class="social"><span></span><span></span><span></span><span></span></div>
    <div class="line"></div>
    <div class="mark"></div>
    <p class="copy">Qondimex, LLC. Copyright © 2017</p>
  </div>
</footer>
</body>
</html>
```